Bramblecrest Capital Partners Needs a Letterhead

Tavi, we need a letterhead/banner for our blog, which is titled "Lantern Horizons". The letterhead/banner should incorporate the enclosed banner image, logo, and the name of our blog ("Lantern Horizons").

We would also like an alternative design that includes our picture. Here, we have two options that we would like to see.

In all, we would like to see 3 different designs: one banner without any pics; and two banner with two versions of our pictures.

The file size should be able to be resized for the space given to us at our website (http://bramblecrest-capital-partners.com).

We also need the letterhead/banner by Friday, June 13. Thanks!!

```html
<!DOCTYPE html>
<html lang="en">
<head>
<meta charset="utf-8">
<title>Lantern Horizons — Bramblecrest Capital Partners</title>
<link rel="stylesheet" href="https://fonts.googleapis.com/css2?family=Questrial&display=swap">
<style>
  :root {
    --canvas-white: #ffffff;
    --warm-glow: #f6e7cf;
    --floor-grey: #dcdcdc;
    --photo-wood: #c9a275;
    --photo-wood-light: #dcbf98;
    --photo-paper: #ece6d8;
    --photo-dark: #2b2b2b;
    --title-gold-dark: #8c7a36;
    --title-gold-light: #cdbb72;
    --title-grey-dark: #4e4e4e;
    --title-grey-light: #a3a3a3;
    --badge-bg: #2b2119;
    --badge-text: #d8c77c;
  }
  * { margin: 0; padding: 0; box-sizing: border-box; }
  html, body { width: 1200px; height: 600px; overflow: hidden; background: var(--canvas-white); }
  .banner {
    position: relative;
    width: 1200px;
    height: 600px;
    overflow: hidden;
    font-family: "Questrial", "Century Gothic", sans-serif;
    background:
      radial-gradient(ellipse 700px 260px at 1000px 0px, var(--warm-glow) 0%, rgba(246,231,207,0) 100%),
      linear-gradient(to bottom, var(--canvas-white) 0%, var(--canvas-white) 88%, var(--floor-grey) 100%);
  }
  .banner__photo {
    position: absolute;
    inset: 0;
    width: 672px;
    height: 540px;
    clip-path: polygon(0 0, 490px 0, 672px 180px, 672px 400px, 420px 470px, 0 540px);
    background:
      linear-gradient(160deg, var(--photo-wood-light) 0%, var(--photo-wood) 45%, var(--photo-paper) 70%, var(--photo-wood) 85%, var(--photo-dark) 100%);
  }
  .banner__photo-reflection {
    position: absolute;
    left: 0;
    top: 400px;
    width: 672px;
    height: 200px;
    clip-path: polygon(0 140px, 420px 70px, 672px 0, 672px 200px, 0 200px);
    background: linear-gradient(to bottom, rgba(200,200,200,0.55) 0%, rgba(255,255,255,0) 90%);
  }
  .banner__title {
    position: absolute;
    left: 768px;
    top: 188px;
    font-weight: 400;
    font-size: 64px;
    line-height: 74px;
    letter-spacing: 0.5px;
  }
  .banner__title span { display: block; -webkit-background-clip: text; background-clip: text; color: transparent; }
  .banner__title-line--gold { background-image: linear-gradient(to bottom, var(--title-gold-light), var(--title-gold-dark)); }
  .banner__title-line--grey { background-image: linear-gradient(to bottom, var(--title-grey-dark), var(--title-grey-light)); }
  .banner__title-reflection {
    position: absolute;
    left: 768px;
    top: 340px;
    font-size: 40px;
    line-height: 40px;
    color: rgba(120,120,120,0.18);
    transform: scaleY(-0.55);
    transform-origin: top;
    filter: blur(1px);
  }
  .banner__brand {
    position: absolute;
    right: 0;
    bottom: 0;
    width: 192px;
    height: 128px;
    background: var(--badge-bg);
    display: flex;
    align-items: flex-end;
    justify-content: center;
    padding: 0 8px 14px;
  }
  .banner__brand-name {
    color: var(--badge-text);
    font-size: 15px;
    line-height: 18px;
    text-align: center;
  }
</style>
</head>
<body>
  <div class="banner">
    <div class="banner__photo" role="img" aria-label="Overhead photo of a wooden desk with keyboard, pen, notebook and a large funding cheque"></div>
    <div class="banner__photo-reflection" aria-hidden="true"></div>

    <h1 class="banner__title">
      <span class="banner__title-line--gold">Lantern</span>
      <span class="banner__title-line--grey">Horizons</span>
    </h1>
    <div class="banner__title-reflection" aria-hidden="true">Lantern Horizons</div>

    <div class="banner__brand">
      <span class="banner__brand-name">Bramblecrest Capital Partners</span>
    </div>
  </div>
</body>
</html>
```